Modern Social Media Ad for Law Firm

We need a crisp ad for social media for our law firm, The Brightmore Firm. The ad will adverrtise for car accident and personal injury cases. Our website is rightfulclaimhelp.com. Our phoone number is 850-314-7582. Use a photo of of our building in the background. I want the add to be light and cripsy. Use logo and photo of attorney. Our address is 418 North Alder Lane at Red Kestrel Fieldhouse.

Target Market(s)

We want to car accident cases and injury cases. The ad should say "Car Accident or Injury? Call us." No fee unless we win!

Industry/Entity Type

Legal

Requirements
Must have
• large photo of me. white background. maybe grayed out columns in the background. website at the bottom with phone number. The Brightmore Firm logo and name at top. Our colors are black and gold with red as an accent color. Should say "Pensacola, FL" at the bottom in small print.
Nice to have
• if you could fade our building into the background that woul dbe nice
Should not have
• no scales of justice -- I want it to be clean, white, crisp, modern

```html
<!DOCTYPE html>
<html lang="en">
<head>
<meta charset="utf-8">
<title>The Brightmore Firm – Social Ads</title>
<link rel="stylesheet" href="https://fonts.googleapis.com/css2?family=Montserrat:wght@500;600;700;800&display=swap">
<style>
:root{
  --stage:#b4b4b4;
  --white:#ffffff;
  --paper:#f3f3f3;
  --ink:#111111;
  --charcoal:#333333;
  --gold:#e2a636;
  --caption:#e2e2e2;
  --suit:#6b6e74;
}
*{margin:0;padding:0;box-sizing:border-box}
html,body{width:1200px;height:407px;overflow:hidden;background:var(--stage);font-family:'Montserrat',sans-serif}
.stage{position:relative;width:1200px;height:407px}
.ad{position:absolute;top:30px;width:347px;height:347px;overflow:hidden;background:var(--white)}
.ad--light-a{left:32px}
.ad--dark{left:426px;background:var(--charcoal)}
.ad--light-b{left:820px}
.building{position:absolute;inset:0;background:linear-gradient(90deg,var(--white) 0%,rgba(238,238,238,.7) 55%,var(--paper) 100%)}
.ad--dark .building{background:linear-gradient(120deg,#3a3a3a,#2c2c2c 60%,#262626)}
.name-band{position:absolute;left:210px;top:0;width:102px;height:230px}
.ad--light-a .name-band{background:linear-gradient(180deg,var(--charcoal) 0%,var(--charcoal) 60%,rgba(51,51,51,0) 100%)}
.ad--light-b .name-band{background:linear-gradient(180deg,var(--gold) 0%,var(--gold) 65%,rgba(226,166,54,0) 100%)}
.name-band__text{position:absolute;top:26px;width:100%;text-align:center;font-weight:700;font-size:16.5px;line-height:18.5px;letter-spacing:.3px;color:var(--white)}
.ad--light-b .name-band__text{color:var(--ink)}
.brand{position:absolute;display:flex;align-items:center;gap:7px;z-index:2}
.brand__mark{width:16px;height:16px;background:var(--gold);flex:none}
.brand__name{font-weight:700;font-size:10.5px;color:var(--ink);white-space:nowrap}
.brand__tag{font-weight:600;font-size:5px;letter-spacing:2.4px;color:var(--ink)}
.ad--light-a .brand{left:20px;top:24px}
.brand-bar{position:absolute;left:0;top:21px;width:210px;height:38px;background:var(--ink)}
.ad--light-b .brand{left:22px;top:28px}
.ad--light-b .brand__name,.ad--light-b .brand__tag{color:var(--white)}
.ad--dark .brand{left:30px;top:140px;flex-direction:column;gap:8px;width:120px}
.ad--dark .brand__mark{width:44px;height:44px}
.ad--dark .brand__name{color:var(--white);font-size:9.5px}
.ad--dark .brand__tag{color:var(--white);letter-spacing:1px;margin-top:-6px}
.case{position:absolute;left:26px;width:136px;height:79px;background:var(--caption)}
.case__photo{position:absolute;left:6px;top:0;width:130px;height:63px}
.case--car{top:74px}
.case--car .case__photo{background:linear-gradient(135deg,#6f7a5c,#8d8e92 45%,#4d4348)}
.case--injury{top:161px}
.case--injury .case__photo{background:linear-gradient(90deg,#d9dadc,#c4c7cc 45%,#2d3a55)}
.case__label{position:absolute;left:5px;bottom:4px;font-weight:600;font-size:7.6px;color:var(--ink)}
.case__label small{font-size:6.6px}
.hero-name{position:absolute;left:27px;top:38px;color:var(--white);line-height:1;z-index:3}
.hero-name__first{display:block;font-weight:500;font-size:37px;letter-spacing:.5px;color:transparent;-webkit-text-stroke:1.1px var(--white)}
.hero-name__last{display:block;font-weight:800;font-size:37px;letter-spacing:.5px;margin-top:3px}
.attorney{position:absolute;z-index:1}
.ad--light-a .attorney,.ad--light-b .attorney{left:196px;top:73px;width:130px;height:274px;border-radius:50px 50px 0 0;background:linear-gradient(180deg,#7b6155 0%,#6f7278 25%,var(--suit) 100%)}
.ad--dark .attorney{left:212px;top:14px;width:135px;height:333px;border-radius:56px 56px 0 0;background:linear-gradient(180deg,#5a4438 0%,#70747b 22%,#5f636a 100%)}
.contact{position:absolute;left:29px;top:257px;color:var(--ink);z-index:2}
.contact__lead{font-weight:600;font-size:8.9px}
.contact__phone{font-weight:800;font-size:19.5px;line-height:21px;color:var(--gold)}
.contact__web{font-weight:600;font-size:9.4px;margin-top:-1px}
.ad--dark .contact{top:260px;color:var(--white)}
.ad--light-b .contact__phone{color:var(--ink)}
.address{position:absolute;left:0;top:305px;font-weight:600;font-size:6.6px;line-height:13px;color:var(--ink);z-index:2}
.address__bar{position:absolute;left:0;top:2px;width:20px;height:15px;background:var(--caption)}
.ad--dark .address__bar,.ad--light-b .address__bar{background:var(--gold)}
.address__pin{position:absolute;left:12px;top:-1px;width:16px;height:16px}
.address__lines{position:absolute;left:31px;top:3px;white-space:nowrap}
.ad--dark .address{color:var(--white)}
</style>
</head>
<body>
<div class="stage">

  <section class="ad ad--light-a">
    <div class="building" role="img" aria-label="Faded photo of the firm's columned building"></div>
    <div class="name-band"><div class="name-band__text">MARCUS<br>HALE</div></div>
    <div class="brand"><span class="brand__mark"></span><div><div class="brand__name">The Brightmore Firm, PLLC</div><div class="brand__tag">ATTORNEYS AT LAW</div></div></div>
    <div class="case case--car"><div class="case__photo" role="img" aria-label="Photo of a crashed car"></div><span class="case__label">Car Accident <small>Cases</small></span></div>
    <div class="case case--injury"><div class="case__photo" role="img" aria-label="Photo of an injured client in a neck brace meeting a lawyer"></div><span class="case__label">Personal Injury Cases</span></div>
    <div class="attorney" role="img" aria-label="Photo of attorney Marcus Hale in a grey suit, arms crossed"></div>
    <div class="contact"><div class="contact__lead">For More Information Contact</div><div class="contact__phone">850-314-7582</div><div class="contact__web">www.rightfulclaimhelp.com</div></div>
    <div class="address"><span class="address__bar"></span>
      <svg class="address__pin" viewBox="0 0 16 16"><circle cx="8" cy="8" r="8" fill="#fff"/><path d="M8 3.5a3 3 0 0 0-3 3c0 2.3 3 5.8 3 5.8s3-3.5 3-5.8a3 3 0 0 0-3-3z" fill="#111"/><circle cx="8" cy="6.5" r="1.1" fill="#fff"/></svg>
      <div class="address__lines">418 North Alder Lane at Red Kestrel Fieldhouse<br>Pensacola, FL</div></div>
  </section>

  <section class="ad ad--dark">
    <div class="building" role="img" aria-label="Dark photo of courthouse columns"></div>
    <div class="attorney" role="img" aria-label="Photo of attorney Marcus Hale standing in a grey suit with a teal tie"></div>
    <div class="hero-name"><span class="hero-name__first">MARCUS</span><span class="hero-name__last">HALE</span></div>
    <div class="brand"><span class="brand__mark"></span><div class="brand__name">The Brightmore Firm, PLLC</div><div class="brand__tag">Attorneys At Law</div></div>
    <div class="contact"><div class="contact__lead">For More Information Contact</div><div class="contact__phone">850-314-7582</div><div class="contact__web">www.rightfulclaimhelp.com</div></div>
    <div class="address"><span class="address__bar"></span>
      <svg class="address__pin" viewBox="0 0 16 16"><circle cx="8" cy="8" r="8" fill="#fff"/><path d="M8 3.5a3 3 0 0 0-3 3c0 2.3 3 5.8 3 5.8s3-3.5 3-5.8a3 3 0 0 0-3-3z" fill="#111"/><circle cx="8" cy="6.5" r="1.1" fill="#fff"/></svg>
      <div class="address__lines">418 North Alder Lane at Red Kestrel Fieldhouse<br>Pensacola, FL</div></div>
  </section>

  <section class="ad ad--light-b">
    <div class="building" role="img" aria-label="Faded photo of the firm's columned building"></div>
    <div class="brand-bar"></div>
    <div class="name-band"><div class="name-band__text">MARCUS<br>HALE</div></div>
    <div class="brand"><span class="brand__mark"></span><div><div class="brand__name">The Brightmore Firm, PLLC</div><div class="brand__tag">ATTORNEYS AT LAW</div></div></div>
    <div class="case case--car"><div class="case__photo" role="img" aria-label="Photo of a crashed car"></div><span class="case__label">Car Accident <small>Cases</small></span></div>
    <div class="case case--injury"><div class="case__photo" role="img" aria-label="Photo of an injured client in a neck brace meeting a lawyer"></div><span class="case__label">Personal Injury Cases</span></div>
    <div class="attorney" role="img" aria-label="Photo of attorney Marcus Hale in a grey suit, arms crossed"></div>
    <div class="contact"><div class="contact__lead">For More Information Contact</div><div class="contact__phone">850-314-7582</div><div class="contact__web">www.rightfulclaimhelp.com</div></div>
    <div class="address"><span class="address__bar"></span>
      <svg class="address__pin" viewBox="0 0 16 16"><circle cx="8" cy="8" r="8" fill="#e2a636"/><path d="M8 3.5a3 3 0 0 0-3 3c0 2.3 3 5.8 3 5.8s3-3.5 3-5.8a3 3 0 0 0-3-3z" fill="#111"/><circle cx="8" cy="6.5" r="1.1" fill="#e2a636"/></svg>
      <div class="address__lines">418 North Alder Lane at Red Kestrel Fieldhouse<br>Pensacola, FL</div></div>
  </section>

</div>
</body>
</html>
```